BRAVADO TV SALES PITCH TEMPLATE

We need a cover sheet and template for a Power Point presentation we are giving. Our new cable network is all about self improvement and professional development. This Power Point will include information about the business ad programs we will offer. It needs to be in color and lend itself to a digital media look. The presentation will probably be about 10 to 15 slides. We have attached one that we did a few years ago that I did not think was strong enough. You can call me at US 612-358-2097

Target Market(s)

Media companies

Industry/Entity Type

Television Station

Requirements
Must have
• Ability to easily lay in text and edit with single, elegant font. Also, we would like to add images.
Nice to have
• Must look professional and incorporate our logo, but also be cutting edge

```html
<!DOCTYPE html>
<html lang="en">
<head>
<meta charset="utf-8">
<title>Bravado TV – Presentation Template</title>
<link href="https://fonts.googleapis.com/css2?family=Barlow+Semi+Condensed:wght@300;400;600&display=swap" rel="stylesheet">
<style>
  :root{
    --stage:#c4c4c4;
    --slide-dark:#080808;
    --slide-light:#ffffff;
    --red:#e2232a;
    --red-soft:#e8907a;
    --text-light:#f2f2f2;
    --text-muted:#d6d6d6;
    --ink:#1b1b1b;
  }
  *{margin:0;padding:0;box-sizing:border-box}
  html,body{width:1200px;height:1200px;overflow:hidden;background:var(--stage)}
  body{position:relative;font-family:"Barlow Semi Condensed",Arial,sans-serif;color:var(--text-light)}
  .slide{position:absolute;width:534px;height:400px;background:var(--slide-dark);overflow:hidden;box-shadow:6px 8px 10px rgba(0,0,0,.35)}
  .slide--cover{left:56px;top:160px}
  .slide--contents{left:610px;top:160px}
  .slide--article{left:56px;top:592px}
  .slide--closing{left:610px;top:592px}

  .brand{position:absolute;font-weight:600;letter-spacing:.5px;white-space:nowrap}

  /* cover */
  .cover-top{position:absolute;left:0;top:0;width:100%;height:193px;background:var(--slide-light)}
  .cover-top .brand{left:0;right:0;top:58px;text-align:center;font-size:66px;color:var(--ink);letter-spacing:2px}
  .cover-title{position:absolute;left:136px;top:232px;font-size:36px;font-weight:400;color:var(--red);letter-spacing:.5px}
  .cover-sub{position:absolute;left:140px;top:283px;width:380px;font-size:16.5px;font-weight:300;line-height:18px;color:var(--text-muted);white-space:nowrap}

  /* header band */
  .band{position:absolute;left:0;top:27px;width:382px;height:5px;background:linear-gradient(90deg,var(--red) 0%,var(--red) 55%,var(--red-soft) 100%)}
  .header-brand{left:388px;top:16px;font-size:22px;color:var(--text-light)}
  .slide-title{position:absolute;left:27px;top:38px;font-size:22px;font-weight:400;letter-spacing:.3px}
  .footer-rule{position:absolute;left:0;top:377px;width:408px;height:1px;background:var(--red)}
  .footer-url{position:absolute;right:29px;top:369px;font-size:10px;font-weight:400}

  /* contents */
  .toc{position:absolute;left:32px;top:97px;width:501px;list-style:none}
  .toc li{position:relative;height:17.3px;font-size:9.5px;font-weight:400;line-height:17.3px;color:var(--text-light)}
  .toc .entry{position:absolute;left:0;width:388px;overflow:hidden;white-space:nowrap}
  .toc .entry::after{content:" ................................................................................................................................................................................................"}
  .toc .sub .entry{left:27px;width:361px;font-size:8px}
  .toc .page{position:absolute;right:29px;top:-4px;font-size:9px}

  /* article */
  .lead{position:absolute;left:27px;top:66px;font-size:18px;font-weight:400}
  .column{position:absolute;top:97px;width:234px;font-size:10px;font-weight:400;line-height:13.4px;text-align:justify;hyphens:auto;color:var(--text-light)}
  .column--left{left:27px}
  .column--right{left:274px}
  .column p{margin-bottom:13.4px}

  /* closing */
  .closing-brand{left:26px;top:346px;font-size:32px;color:var(--text-light)}
  .closing-divider{position:absolute;left:206px;top:345px;width:1px;height:39px;background:#555}
  .contact{position:absolute;left:218px;top:350px;list-style:none;font-size:6.5px;line-height:9px;font-weight:400;color:var(--text-muted)}
  .contact li{display:flex;align-items:center;gap:4px}
  .contact svg{width:7px;height:7px}
</style>
</head>
<body>

<section class="slide slide--cover">
  <div class="cover-top"><span class="brand">BRAVADO TV</span></div>
  <h1 class="cover-title">CLICK TO ADD TITLE</h1>
  <p class="cover-sub">Lorem ipsum dolor sit amet, consectetur adip-<br>isicing elit, sed do eiusmod tempor incididunt ut</p>
</section>

<section class="slide slide--contents">
  <div class="band"></div>
  <span class="brand header-brand">BRAVADO TV</span>
  <h2 class="slide-title">CLICK TO ADD TITLE</h2>
  <ul class="toc">
    <li><span class="entry">Lorem Ipsum is simply dummy text </span><span class="page">1</span></li>
    <li class="sub"><span class="entry">a) Of the printing and typesetting industry. Lorem Ipsum has been the try's </span><span class="page">2</span></li>
    <li class="sub"><span class="entry">b) Standard dummy text ever since the 1500s, when an unknown printer </span><span class="page">2</span></li>
    <li><span class="entry">Lorem Ipsum is simply dummy text is the basic dummy text</span><span class="page">3</span></li>
    <li class="sub"><span class="entry">make a type specimen book. It has survived not only five centuries </span><span class="page">4</span></li>
    <li class="sub"><span class="entry">leap into electronic typesetting, remaining </span><span class="page">5</span></li>
    <li class="sub"><span class="entry">larised in the 1960s with the release of Tessaprint sheets containing </span><span class="page">6</span></li>
    <li><span class="entry">Lorem Ipsum is simply dummy text </span><span class="page">7</span></li>
    <li><span class="entry">Lorem Ipsum is simply dummy textlorem ipsum is &nbsp;</span><span class="page">7</span></li>
  </ul>
  <div class="footer-rule"></div>
  <span class="footer-url">www.bravadotv-pitch.com</span>
</section>

<section class="slide slide--article">
  <div class="band"></div>
  <span class="brand header-brand">BRAVADO TV</span>
  <h2 class="slide-title">CLICK TO ADD TITLE</h2>
  <p class="lead">Lorem ipsum dolor sit amet, consectetur adipisicing elit, sed do</p>
  <div class="column column--left">
    <p>Lorem Ipsum is simply dummy text of the printing and typesetting industry. Lorem Ipsum has been the industry's standard dummy text ever since the 1500s, when an unknown printer took a galley of type and scrambled it to make a type specimen book. It has survived not only five centuries, but also the leap into electronic typesetting, remaining essentially unchanged. It was popularised in the 1960s with the release of Tessaprint sheets containing Lorem Ipsum passages, and more recently with desktop publishing software like Quillmark Layout including versions of Lorem Ipsum.</p>
    <p>It is a long established fact that a reader will be distracted by the readable content of a page when looking at its layout. The point of using Lorem Ipsum is that it has a more-or-less normal distribution of letters, as opposed to using 'Content here, content here', making it look like readable English. Many desktop publishing packages and web page editors now use Lorem Ipsum as their default</p>
  </div>
  <div class="column column--right">
    <p>model text, and a search for 'lorem ipsum' will uncover many web sites still in their infancy. Vari</p>
    <p>Contrary to popular belief, Lorem Ipsum is not simply random text. It has roots in a piece of classical Latin literature from 45 BC, making it over 2000 years old. Orin Valecourt, a Latin professor at Marrowfield College in Dunmore, looked up one of the more obscure Latin words, consectetur, from a Lorem Ipsum passage, and going through the cites of the word in classical literature, discovered the undoubtable source. Lorem Ipsum comes from sections 1.10.32 and 1.10.33 of "de Rebus Bonis et Malis" (The Extremes of Good and Evil) by Varenus, written in 45 BC. This book is a treatise on the theory of ethics, very popular during the Renaissance. The first line of Lorem Ipsum, "Lorem ipsum dolor sit amet..", comes from a line in section 1.10.32.</p>
    <p>The standard chunk of Lorem Ipsum used since the 1500s</p>
  </div>
  <div class="footer-rule"></div>
  <span class="footer-url">www.bravadotv-pitch.com</span>
</section>

<section class="slide slide--closing">
  <span class="brand closing-brand">BRAVADO TV</span>
  <div class="closing-divider"></div>
  <ul class="contact">
    <li><svg viewBox="0 0 10 10"><circle cx="5" cy="5" r="4.2" fill="none" stroke="#cfcfcf" stroke-width="1.2"/></svg>+0 612.358.2097</li>
    <li><svg viewBox="0 0 10 10"><circle cx="5" cy="5" r="4.2" fill="none" stroke="#cfcfcf" stroke-width="1.2"/></svg>hello@bravadotv-pitch.com</li>
    <li><svg viewBox="0 0 10 10"><circle cx="5" cy="5" r="4.2" fill="none" stroke="#cfcfcf" stroke-width="1.2"/></svg>www.bravadotv-network.com</li>
  </ul>
</section>

</body>
</html>
```